I am a Life Coaching and I have purchased the logo for my business. I need business cards

I need a business card design using the logo attached (but instead of the logo saying "Harbor" I need it to say "Open Horizon Coaching"

Target Market(s)

Middle-aged people

Industry/Entity Type

Life coaching

Contact Information for Business Card

Name, email address, phone number, website

Font styles to use
Serif
Sans Serif
Script

Colors
0094D4
00A9DD
6FCCEA
C7EBF8
E9F6FB
00AB8E
00BBA5
67D7C9
C6EFE9
E9F9F6
59FF00
82FF00
B8FF75
E3FFCB
F4FFEA

Requirements
Must have
• Logo and contact info above
Nice to have
• As close to the business card inspo attached as possible

```html
<!DOCTYPE html>
<html lang="en">
<head>
<meta charset="utf-8">
<title>Open Horizon Coaching – Business Cards</title>
<link href="https://fonts.googleapis.com/css2?family=Caveat:wght@500&family=Poppins:wght@400&display=swap" rel="stylesheet">
<style>
  :root {
    --backdrop: #2b2b2d;
    --card: #ffffff;
    --blue-deep: #0094d4;
    --blue: #00a9dd;
    --blue-soft: #6fccea;
    --blue-pale: #c7ebf8;
    --teal: #00ab8e;
    --teal-mid: #00bba5;
    --green: #82ff00;
    --green-soft: #b8e86a;
    --green-pale: #e3ffcb;
    --ink: #1d1d1f;
  }
  * { box-sizing: border-box; margin: 0; padding: 0; }
  html, body {
    width: 1200px; height: 880px; overflow: hidden;
    background: var(--backdrop);
  }
  .stage { position: relative; width: 1200px; height: 880px; }

  .card {
    position: absolute;
    width: 560px; height: 320px;
    background: var(--card);
    overflow: hidden;
    box-shadow: 0 10px 30px rgba(0,0,0,.45);
  }
  .card--front { left: 70px; top: 70px; }
  .card--back  { left: 570px; top: 480px; }

  /* front */
  .wash-band {
    position: absolute; left: 0; right: 0; height: 74px;
    background: linear-gradient(90deg, var(--green-soft) 0%, var(--green-pale) 35%, #c9ec8e 55%, var(--blue-pale) 80%, var(--blue-soft) 100%);
    opacity: .9;
  }
  .wash-band--top { top: 0; }
  .wash-band--bottom {
    bottom: 0;
    background: linear-gradient(90deg, var(--blue-soft) 0%, var(--blue-pale) 25%, #c9ec8e 50%, var(--green-soft) 75%, var(--green-pale) 100%);
  }
  .rule {
    position: absolute; left: 0; right: 0; height: 3px;
    background: linear-gradient(90deg, var(--blue-pale), var(--blue-deep));
  }
  .rule--top { top: 74px; }
  .rule--bottom { bottom: 74px; background: linear-gradient(90deg, var(--blue-deep), var(--blue-pale)); }

  .brand {
    display: flex; align-items: center; gap: 10px;
    font-family: "Caveat", cursive; font-weight: 500;
    color: var(--ink); white-space: nowrap;
  }
  .brand__dot {
    width: 16px; height: 16px; border-radius: 50%;
    background: var(--blue-soft); flex: none;
  }
  .card--front .brand {
    position: absolute; left: 0; right: 0; top: 140px;
    justify-content: center; font-size: 38px;
  }

  /* back */
  .leaf-art {
    position: absolute; left: 50px; top: 90px; width: 190px; height: 230px;
    background: linear-gradient(160deg, var(--blue-soft) 0%, var(--blue-pale) 35%, var(--green-pale) 65%, #a9dcc9 100%);
    border-radius: 50% 50% 8px 8px / 40% 40% 8px 8px;
    opacity: .85;
  }
  .card--back .brand {
    position: absolute; left: 270px; top: 44px; font-size: 28px;
  }
  .card--back .brand__dot { width: 14px; height: 14px; }
  .contact {
    position: absolute; left: 280px; top: 108px;
    font-family: "Poppins", sans-serif;
  }
  .contact__name {
    font-family: "Caveat", cursive; font-weight: 500;
    font-size: 30px; color: var(--blue-deep); line-height: 1;
  }
  .contact__role {
    font-size: 10px; letter-spacing: 6px; color: var(--blue-soft);
    margin: 4px 0 14px 4px;
  }
  .contact__list { list-style: none; }
  .contact__item {
    display: flex; align-items: center; gap: 8px;
    font-size: 13px; color: var(--teal-mid); line-height: 22px;
    white-space: nowrap;
  }
  .contact__item svg { width: 12px; height: 12px; flex: none; }
  .contact__social-mark {
    width: 11px; height: 11px; border-radius: 50%;
    border: 1.5px solid var(--teal-mid); flex: none;
  }
</style>
</head>
<body>
<main class="stage">

  <section class="card card--front" aria-label="Card front">
    <div class="wash-band wash-band--top" role="img" aria-label="Watercolour wash in green and blue"></div>
    <div class="rule rule--top"></div>
    <div class="brand"><span class="brand__dot"></span>Open Horizon Coaching</div>
    <div class="rule rule--bottom"></div>
    <div class="wash-band wash-band--bottom" role="img" aria-label="Watercolour wash in blue and green"></div>
  </section>

  <section class="card card--back" aria-label="Card back">
    <div class="leaf-art" role="img" aria-label="Watercolour leafy branch in blue and green"></div>
    <div class="brand"><span class="brand__dot"></span>Open Horizon Coaching</div>
    <div class="contact">
      <p class="contact__name">Daniel Whitmore</p>
      <p class="contact__role">LIFE COACH</p>
      <ul class="contact__list">
        <li class="contact__item">
          <svg viewBox="0 0 24 24" fill="var(--teal-mid)"><path d="M6.6 10.8a15 15 0 0 0 6.6 6.6l2.2-2.2a1 1 0 0 1 1-.25 11.4 11.4 0 0 0 3.6.57 1 1 0 0 1 1 1V20a1 1 0 0 1-1 1A17 17 0 0 1 3 4a1 1 0 0 1 1-1h3.5a1 1 0 0 1 1 1c0 1.250.2 2.45.57 3.6a1 1 0 0 1-.25 1z"/></svg>
          555-014-2290
        </li>
        <li class="contact__item">
          <svg viewBox="0 0 24 24" fill="none" stroke="var(--teal-mid)" stroke-width="2"><rect x="3" y="5" width="18" height="14" rx="1"/><path d="M3 6l9 7 9-7"/></svg>
          info@openhorizoncoaching.com
        </li>
        <li class="contact__item">
          <svg viewBox="0 0 24 24" fill="none" stroke="var(--teal-mid)" stroke-width="2"><circle cx="12" cy="12" r="9"/><path d="M3 12h18M12 3c3 3 3 15 0 18M12 3c-3 3-3 15 0 18"/></svg>
          www.openhorizoncoaching.com
        </li>
        <li class="contact__item">
          <span class="contact__social-mark"></span>
          openhorizoncoaching
        </li>
      </ul>
    </div>
  </section>

</main>
</body>
</html>
```